Signage. Will be for store front. Building is on a corner lot. Lots of traffic.

Opening a new location for our landscape business with a garden store (boutique theme) which will have big pottery pots, house plants, ferns and orchids for sale.

And on the side lot of the store we will have bigger bulk items(contractors theme) landscape plants, sod, mulch, soil, rock for sale.

Sign is about 8’x6’

Target Market(s)

Home owners
Landscapers
Builders

Industry/Entity Type

Landscaping

Font styles to use
Sans Serif

Colors
9bcb3c

Requirements
Must have
• “ Installation and Delivery” is a big deal to let people know we do that
Nice to have
• Added a first rendition idea but don’t love it
Added a file with some words to play with
Need help with the words
Should not have
• ?

```html
<!DOCTYPE html>
<html lang="en">
<head>
<meta charset="utf-8">
<title>Fernbrook Gardens – Storefront Sign</title>
<link rel="stylesheet" href="https://fonts.googleapis.com/css2?family=Passion+One:wght@400;700&display=swap">
<style>
  :root {
    --brand-lime: #9bcb3c;
    --leaf-green: #6a9a3a;
    --deep-green: #0f4a2a;
    --paper: #ffffff;
    --grass-dark: #2f7a2a;
    --grass-light: #7cc24a;
  }
  html, body {
    margin: 0;
    padding: 0;
    width: 1200px;
    height: 800px;
    overflow: hidden;
    background: #eef1ea;
  }
  .sign {
    position: relative;
    width: 1200px;
    height: 800px;
    background: var(--paper);
    overflow: hidden;
    font-family: "Passion One", sans-serif;
  }
  .sign__frame {
    position: absolute;
    inset: 0;
    pointer-events: none;
    box-shadow:
      inset 0 0 60px 30px rgba(155, 203, 60, 0.55),
      inset 0 60px 70px -20px rgba(106, 154, 58, 0.6);
  }
  .feature-image {
    position: absolute;
    left: 30px;
    top: 120px;
    width: 356px;
    height: 480px;
    border-radius: 50% 50% 50% 50% / 62% 62% 38% 38%;
    background: linear-gradient(180deg, #6f8f3a 0%, #4f6a2c 45%, #3a3424 100%);
  }
  .brand {
    position: absolute;
    left: 460px;
    top: 66px;
    display: flex;
    align-items: center;
    gap: 24px;
  }
  .brand__name {
    margin: 0;
    font-weight: 400;
    font-size: 70px;
    line-height: 0.95;
    color: var(--deep-green);
    letter-spacing: 2px;
    text-transform: uppercase;
  }
  .brand__dot {
    width: 66px;
    height: 66px;
    border-radius: 50%;
    background: var(--brand-lime);
  }
  .headline {
    position: absolute;
    left: 400px;
    top: 240px;
    width: 780px;
    margin: 0;
    text-align: center;
    font-weight: 700;
    font-size: 68px;
    line-height: 1.0;
    color: var(--deep-green);
    text-transform: uppercase;
  }
  .services {
    position: absolute;
    top: 478px;
    margin: 0;
    padding: 0;
    list-style: none;
    font-weight: 400;
    font-size: 34px;
    line-height: 1;
    color: var(--deep-green);
    text-transform: uppercase;
  }
  .services--left { left: 415px; }
  .services--right { left: 830px; top: 472px; }
  .services li {
    position: relative;
    padding-left: 22px;
    margin-bottom: 11px;
  }
  .services li::before {
    content: "";
    position: absolute;
    left: 0;
    top: 11px;
    width: 10px;
    height: 10px;
    border-radius: 50%;
    background: var(--deep-green);
  }
  .grass {
    position: absolute;
    left: 0;
    right: 0;
    bottom: 0;
    height: 62px;
    background: linear-gradient(180deg, rgba(124,194,74,0) 0%, var(--grass-light) 30%, var(--grass-dark) 100%);
  }
</style>
</head>
<body>
  <main class="sign">
    <div class="feature-image" role="img" aria-label="Photo of landscapers installing plants and sod in a garden"></div>

    <header class="brand">
      <h1 class="brand__name">Fernbrook<br>Gardens</h1>
      <span class="brand__dot"></span>
    </header>

    <h2 class="headline">Sod | All Varieties |<br>Delivery | Removal |<br>Installation</h2>

    <ul class="services services--left">
      <li>Garden Center</li>
      <li>Landscape Supply</li>
      <li>Garden Shop</li>
      <li>Garden Supply</li>
      <li>Lawn &amp; Garden</li>
    </ul>
    <ul class="services services--right">
      <li>Nursery &amp;<br>Garden</li>
      <li>Nursery</li>
      <li>Sod</li>
      <li>Landscaping</li>
    </ul>

    <div class="grass" role="img" aria-label="Band of green grass along the bottom edge"></div>
    <div class="sign__frame"></div>
  </main>
</body>
</html>
```